Software Company Requires Website

We need a web design for a new mobile software development company based in London named Velquin Solutions.
The design needs to be clean and smooth. Not too flashy, not too boring.
I would like to try the design with some warm colors, and maybe a headline or something highlighted with a strong color. ( logo ? ) The layout should be something like the bellow links, all in one page.

http://brantelo.net/
http://www.kelvory.com/
http://www.work-plover.de/
http://www.tusker.com/
http://www.quildenta.com/us/

Now some of them they seem different from the others, but in each of them there is something that ticks my brain, so it`s up to you to surprise me.

I have uploaded the logo of the company, so you guys can fit that in your design as well.
Updates

Hy everybody This will be the last update for the brief. The company will focus in the beginning for mobile development only, so i would like the website design to be done in a matter that will reflect that. We will develop IOS, Mobile and Windows applications. We will also require 3 pages: One for the home menu, one for portfolio and one for contact us. The layout should be the same ( one page scroll down ) but the design of the 3 pages different. Please readdress the brief. Hope that i provided enough information for the scope of the project.

I have uploaded the logo that you guys can use. If the logo requires small modifications you can adjust that to suit your idea as long as the logo does not change completely.

Target Market(s)

High End companies that require simplified software solutions.

Industry/Entity Type

It Company

Number of Pages Required

3 page

Requirements
Must have
• One page scroll down layout for 3 pages:
• one for home page, one for portfolio and one for contact us.
• In the portfolio page we would like to have different display options for given examples of applications ( min 3 )

```html
<!DOCTYPE html>
<html lang="en">
<head>
<meta charset="utf-8">
<title>Velquin Solutions</title>
<link rel="stylesheet" href="https://fonts.googleapis.com/css2?family=Oswald:wght@400;500&family=Montserrat:wght@300;600&family=Open+Sans:wght@400;600;700&display=swap">
<style>
:root{
  --blue:#1b8ee0;
  --blue-dark:#1577c2;
  --navy:#06111f;
  --navy-mid:#0d2440;
  --page:#e4e9ef;
  --panel:#ffffff;
  --ink:#1d1f22;
  --muted:#7c8389;
  --line:#e3e6ea;
  --yellow:#f2c200;
  --footer:#ececec;
}
*{margin:0;padding:0;box-sizing:border-box}
html,body{width:1200px;height:2462px;overflow:hidden}
body{position:relative;background:var(--page);font-family:"Open Sans",Arial,sans-serif;color:var(--ink)}
.abs{position:absolute}

/* header */
.site-header{left:0;top:0;width:1200px;height:102px;background:#f4f5f6}
.brand{left:107px;top:28px;display:flex;align-items:center;gap:12px}
.brand-mark{width:34px;height:34px;border-radius:50%;background:var(--blue)}
.brand-name{font-family:"Open Sans",sans-serif;font-weight:600;font-size:28px;color:var(--blue);letter-spacing:.5px}
.header-social{left:865px;top:17px;display:flex;gap:11px;align-items:center}
.header-social .dot{width:22px;height:22px;border-radius:50%;background:#9aa1a7}
.header-divider{left:852px;top:16px;width:1px;height:24px;background:#c9cdd1}
.header-divider.two{left:940px}
.header-contact{left:955px;top:21px;font-size:13px;color:#7b8288;display:flex;gap:8px;align-items:center}
.search-tab{left:1046px;top:0;width:41px;height:62px;background:var(--blue);display:flex;align-items:center;justify-content:center}
.main-nav{right:170px;top:54px;display:flex;gap:24px;font-size:14.5px;color:#50585f}
.main-nav .active{color:var(--blue);font-weight:700}

/* hero */
.hero{left:0;top:102px;width:1200px;height:650px;background:radial-gradient(ellipse at 48% 30%,#17406e 0%,var(--navy-mid) 30%,var(--navy) 70%)}
.hero-intro{left:113px;top:232px;font-family:"Oswald",sans-serif;font-size:31px;color:#fff}
.hero-title{left:113px;top:268px;font-family:"Oswald",sans-serif;font-weight:500;font-size:60px;line-height:66px;color:#fff;letter-spacing:.5px}
.hero-title .accent{color:var(--blue)}
.hero-sub{left:113px;top:420px;font-size:23px;color:#fff}
.hero-sub b{font-weight:700}
.btn-more{left:112px;top:463px;width:141px;height:44px;background:var(--blue);color:#fff;font-size:16px;display:flex;align-items:center;justify-content:center;gap:10px;letter-spacing:.5px}
.hero-dots{left:130px;top:645px;width:400px;height:20px}
.hero-visual{left:530px;top:176px;width:540px;height:500px;border-radius:40px 40px 0 0;background:linear-gradient(160deg,#2a2c30 0%,#3a3330 40%,#c79a82 75%,#b48470 100%)}

/* panels */
.panel{background:var(--panel);box-shadow:0 1px 3px rgba(0,0,0,.08)}
.features{left:107px;top:676px;width:978px;height:352px}
.showcase{left:107px;top:1037px;width:978px;height:938px}
.section-title{position:absolute;left:0;width:100%;text-align:center;font-family:"Montserrat",sans-serif;font-weight:300;font-size:32px;line-height:44px;color:var(--ink)}
.section-title b{font-weight:600}
.section-sub{position:absolute;left:0;width:100%;text-align:center;font-size:12.5px;line-height:17px;color:var(--muted)}
.feature{position:absolute;width:170px;margin-left:-85px;text-align:center;top:134px}
.feature .ring{width:124px;height:124px;margin:0 auto;border-radius:50%;border:4px solid var(--blue);display:flex;align-items:center;justify-content:center;background:#fff}
.feature.active .ring{background:var(--blue)}
.feature .label{margin-top:22px;font-size:13.5px;color:#33383d}
.feature.active .label{color:var(--blue)}

.tile{position:absolute}
.tile-a{left:28px;top:133px;width:302px;height:151px;background:linear-gradient(135deg,#6c7378,#3a3f44)}
.tile-b{left:28px;top:293px;width:302px;height:236px;background:linear-gradient(135deg,#f7c22a,#f59f0e)}
.tile-c{left:336px;top:133px;width:302px;height:268px;background:radial-gradient(circle at 50% 55%,#7fc3e8,#f1f3f5 70%)}
.tile-d{left:336px;top:408px;width:302px;height:121px;background:linear-gradient(90deg,#0c0f14,#2c3540)}
.tile-e{left:646px;top:133px;width:302px;height:237px;background:linear-gradient(180deg,#ece2dc,#c7a987)}
.tile-f{left:646px;top:378px;width:302px;height:151px;background:linear-gradient(135deg,#1c1f24 35%,#f0f2f4 36%)}
.divider{position:absolute;left:28px;top:572px;width:920px;height:1px;background:var(--line)}
.member{position:absolute;top:706px;width:180px;margin-left:-90px;text-align:center}
.member .avatar{width:148px;height:148px;margin:0 auto;border-radius:50%}
.member .name{margin-top:12px;font-size:15px;font-weight:700;color:#1e2226}
.member .role{font-size:13.5px;color:#4a5056}

/* contact */
.contact-band{left:0;top:1926px;width:1200px;height:459px;background:radial-gradient(ellipse at 20% 40%,#15355a 0%,var(--navy-mid) 30%,var(--navy) 75%)}
.contact-band .section-title{top:122px;color:#fff}
.contact-band .section-sub{top:172px;color:#8a96a3}
.contact-list{position:absolute;left:112px;top:237px;color:#fff;font-size:13.5px}
.contact-list li{list-style:none;display:flex;gap:12px;align-items:flex-start;margin-bottom:16px;line-height:18px}
.field{position:absolute;background:#fff;font-size:13.5px;color:#3a3f44;padding:14px 12px}
.f-name{left:409px;top:221px;width:259px;height:45px}
.f-email{left:409px;top:274px;width:259px;height:45px}
.f-phone{left:409px;top:326px;width:259px;height:45px}
.f-msg{left:676px;top:221px;width:409px;height:150px;padding-top:11px}
.btn-send{position:absolute;left:975px;top:382px;width:110px;height:38px;background:var(--yellow);color:#fff;font-weight:700;font-size:14px;display:flex;align-items:center;justify-content:center;letter-spacing:.3px}
.to-top{left:583px;top:2366px;width:34px;height:36px;background:#fff;display:flex;align-items:center;justify-content:center}
.site-footer{left:0;top:2385px;width:1200px;height:77px;background:var(--footer);text-align:center;font-size:12.5px;color:#6b7177;padding-top:33px}
</style>
</head>
<body>

<header class="site-header abs">
  <div class="brand abs"><span class="brand-mark"></span><span class="brand-name">Velquin Solutions</span></div>
  <span class="header-divider abs"></span>
  <div class="header-social abs"><span class="dot"></span><span class="dot"></span></div>
  <span class="header-divider two abs"></span>
  <div class="header-contact abs">
    <svg width="16" height="14" viewBox="0 0 16 14"><path d="M1 7 8 1l7 6v6H1z" fill="#8a9197"/></svg>Contact
  </div>
  <div class="search-tab abs">
    <svg width="24" height="24" viewBox="0 0 24 24"><circle cx="10" cy="10" r="7" fill="none" stroke="#fff" stroke-width="3"/><path d="M15 15l6 6" stroke="#fff" stroke-width="3.5" stroke-linecap="round"/></svg>
  </div>
  <nav class="main-nav abs">
    <span class="active">HOME</span><span>About Us</span><span>Our Services</span><span>Portfolio</span><span>Contact Us</span>
  </nav>
</header>

<section class="hero abs"></section>
<div class="hero-visual abs" role="img" aria-label="Hand holding a smartphone showing a social music app"></div>
<div class="hero-intro abs">We are a</div>
<h1 class="hero-title abs">CREATIVE <span class="accent">SOFTWEAR</span><br>DEVELOPER</h1>
<p class="hero-sub abs">Speializing in <b>Mobile Apps</b></p>
<div class="btn-more abs">READ MORE
  <svg width="9" height="13" viewBox="0 0 9 13"><path d="M2 1l5 5.5L2 12" fill="none" stroke="#fff" stroke-width="2"/></svg>
</div>
<svg class="hero-dots abs" viewBox="0 0 400 20">
  <line x1="0" y1="10" x2="400" y2="10" stroke="#2b5278" stroke-width="1"/>
  <circle cx="18" cy="10" r="7" fill="#3a4f66"/>
  <circle cx="54" cy="10" r="7" fill="var(--blue)"/>
  <circle cx="92" cy="10" r="7" fill="#3a4f66"/>
</svg>

<section class="features panel abs">
  <h2 class="section-title" style="top:28px">Features that our <b>Customers love</b></h2>
  <p class="section-sub" style="top:71px">Neque porro quisquam est qui dolorem ipsum quia dolor sit amet, consectetur, adipisci velit...</p>

  <div class="feature active" style="left:105px">
    <div class="ring"><svg width="40" height="64" viewBox="0 0 40 64"><rect x="3" y="3" width="34" height="58" rx="5" fill="none" stroke="#fff" stroke-width="3"/><line x1="3" y1="12" x2="37" y2="12" stroke="#fff" stroke-width="2"/><line x1="3" y1="50" x2="37" y2="50" stroke="#fff" stroke-width="2"/><circle cx="20" cy="56" r="2.5" fill="#fff"/></svg></div>
    <div class="label">Mobile</div>
  </div>
  <div class="feature" style="left:253px">
    <div class="ring"><svg width="66" height="40" viewBox="0 0 66 40"><rect x="24" y="6" width="38" height="28" fill="none" stroke="var(--blue)" stroke-width="3"/><path d="M24 6l19 16 19-16" fill="none" stroke="var(--blue)" stroke-width="3"/><path d="M2 12h16M6 20h12M10 28h8" stroke="var(--blue)" stroke-width="3"/></svg></div>
    <div class="label">Email Campaigns</div>
  </div>
  <div class="feature" style="left:405px">
    <div class="ring"><svg width="50" height="44" viewBox="0 0 50 44"><rect x="4" y="28" width="8" height="14" fill="var(--blue)"/><rect x="16" y="22" width="8" height="20" fill="var(--blue)"/><rect x="28" y="26" width="8" height="16" fill="var(--blue)"/><rect x="40" y="16" width="8" height="26" fill="var(--blue)"/><path d="M4 20l14-10 10 6L44 4" fill="none" stroke="var(--blue)" stroke-width="3"/><path d="M36 3h9v9" fill="none" stroke="var(--blue)" stroke-width="3"/></svg></div>
    <div class="label">Data Capture</div>
  </div>
  <div class="feature" style="left:559px">
    <div class="ring"><svg width="52" height="52" viewBox="0 0 52 52"><circle cx="26" cy="26" r="23" fill="var(--blue)"/><ellipse cx="18" cy="20" rx="3" ry="4" fill="#fff"/><ellipse cx="34" cy="20" rx="3" ry="4" fill="#fff"/><path d="M14 30q12 12 24 0z" fill="#fff"/></svg></div>
    <div class="label">Customer Segmentation</div>
  </div>
  <div class="feature" style="left:712px">
    <div class="ring"><svg width="56" height="46" viewBox="0 0 56 46"><path d="M4 14h48l-6 28H10z" fill="var(--blue)"/><path d="M16 14 26 2M40 14 30 2" stroke="var(--blue)" stroke-width="3"/><path d="M18 20v16M26 20v16M34 20v16" stroke="#fff" stroke-width="3"/><circle cx="44" cy="36" r="7" fill="#fff" stroke="var(--blue)" stroke-width="2"/><path d="M41 36l2 2 4-4" fill="none" stroke="var(--blue)" stroke-width="2"/></svg></div>
    <div class="label">Dynamic Offers</div>
  </div>
  <div class="feature" style="left:866px">
    <div class="ring"><svg width="58" height="52" viewBox="0 0 58 52"><rect x="22" y="2" width="14" height="10" fill="var(--blue)"/><rect x="2" y="22" width="14" height="10" fill="var(--blue)"/><rect x="42" y="22" width="14" height="10" fill="var(--blue)"/><rect x="22" y="40" width="14" height="10" fill="var(--blue)"/><path d="M29 12v28M16 27h26" stroke="var(--blue)" stroke-width="2.5"/></svg></div>
    <div class="label">Up- Sell and Cross-Sell</div>
  </div>
</section>

<section class="showcase panel abs">
  <h2 class="section-title" style="top:41px">Our <b>Portfolio</b></h2>
  <p class="section-sub" style="top:86px">Neque porro quisquam est qui dolorem ipsum quia dolor sit amet, consectetur, adipisci velit...</p>

  <div class="tile tile-a" role="img" aria-label="Smartphone with earphones on a grey surface"></div>
  <div class="tile tile-b" role="img" aria-label="Branding and creative portfolio cover on yellow paint"></div>
  <div class="tile tile-c" role="img" aria-label="Smartphone surrounded by colourful app icons"></div>
  <div class="tile tile-d" role="img" aria-label="Smartphone apps for business users banner"></div>
  <div class="tile tile-e" role="img" aria-label="Cartoon characters beside a desktop screen showing a website"></div>
  <div class="tile tile-f" role="img" aria-label="Mobile application development banner with app icons"></div>

  <div class="divider"></div>

  <h2 class="section-title" style="top:615px">Our <b>Team</b></h2>
  <p class="section-sub" style="top:658px">Neque porro quisquam est qui dolorem ipsum quia dolor sit amet, consectetur, adipisci velit...</p>

  <div class="member" style="left:177px">
    <div class="avatar" role="img" aria-label="Portrait of team member" style="background:linear-gradient(160deg,#dfe4e8,#3a4450)"></div>
    <div class="name">Aron Feldway</div><div class="role">Lorem lipsum</div>
  </div>
  <div class="member" style="left:371px">
    <div class="avatar" role="img" aria-label="Portrait of team member" style="background:linear-gradient(160deg,#7a3a1e,#2a1a14)"></div>
    <div class="name">Mara Quillon</div><div class="role">Lorem lipsum</div>
  </div>
  <div class="member" style="left:563px">
    <div class="avatar" role="img" aria-label="Portrait of team member" style="background:linear-gradient(160deg,#2a2e33,#6b584a)"></div>
    <div class="name">Edin Tolvar</div><div class="role">Lorem lipsum</div>
  </div>
  <div class="member" style="left:756px">
    <div class="avatar" role="img" aria-label="Portrait of team member" style="background:linear-gradient(160deg,#c9d6df,#8a6d55)"></div>
    <div class="name">Dolar sit amet</div><div class="role">Lorem lipsum</div>
  </div>
</section>

<section class="contact-band abs" style="z-index:-1"></section>
<section class="contact-band abs" style="background:none">
  <h2 class="section-title">Contact <b>Us</b></h2>
  <p class="section-sub">Neque porro quisquam est qui dolorem ipsum quia dolor sit amet, consectetur, adipisci velit...</p>
  <ul class="contact-list">
    <li><svg width="14" height="14" viewBox="0 0 14 14"><path d="M3 1l3 3-2 2q1 3 4 4l2-2 3 3-2 2Q4 13 1 3z" fill="#fff"/></svg>Call Us: 0800 (312) 4468</li>
    <li><svg width="16" height="12" viewBox="0 0 16 12"><rect width="16" height="12" fill="#fff"/><path d="M0 0l8 7 8-7" fill="none" stroke="var(--navy)" stroke-width="1.5"/></svg>Email: info@velquin.com</li>
    <li><svg width="18" height="16" viewBox="0 0 18 16"><rect x="1" y="6" width="16" height="9" rx="2" fill="#fff"/><rect x="4" y="1" width="10" height="6" fill="none" stroke="#fff" stroke-width="1.5"/></svg><span>Need to fax us? here you go!<br>123 555 0148</span></li>
  </ul>
  <div class="field f-name">Name</div>
  <div class="field f-email">Email</div>
  <div class="field f-phone">Phone</div>
  <div class="field f-msg">Message</div>
  <div class="btn-send">SEND NOW</div>
</section>

<div class="to-top abs">
  <svg width="16" height="18" viewBox="0 0 16 18"><path d="M8 17V3M2 8l6-6 6 6" fill="none" stroke="var(--navy)" stroke-width="2.5"/></svg>
</div>

<footer class="site-footer abs">Copyrights ©2014 VelquinSolutions.com - All Rights reserved</footer>

</body>
</html>
```